Supplement label for Brain health

I need a design for a supplement this supplement is a brain boost supplement.

The Name is Cortiva Plus.

I have attached other labels I like. This is for 50 plus demographic so the lettering needs to be easy to read and stand out. I have attached a dummy label template that once the winner is choosen then they will get the real supplement facts etc.

Clean desgin easy to read.

This file must be finished in AI format.

Target Market(s)

50 plus 70 percent female 30 percent male

Industry/Entity Type

Supplement

Font styles to use
Other font styles liked:
• Myrid pro maybe

Requirements
Must have
• easy to read text so no colors that hide text or hard to read.

```html
<!DOCTYPE html>
<html lang="en">
<head>
<meta charset="UTF-8">
<title>Cortiva Plus – Brain Booster Supplement Label</title>
<link href="https://fonts.googleapis.com/css2?family=Oswald:wght@600;700&family=Open+Sans:wght@400;700&family=Roboto+Condensed:wght@700&display=swap" rel="stylesheet">
<style>
  :root {
    --page-bg: #e9e9ea;
    --label-white: #ffffff;
    --band-orange: #ef8a1d;
    --tab-navy: #173c8c;
    --tab-navy-light: #2350a8;
    --title-orange: #d2591c;
    --title-rust: #a93c12;
    --wave-light: #3db0e5;
    --wave-navy: #1b3684;
    --wave-blue: #2a80d2;
    --wave-blue-deep: #1a5eb1;
    --brain-glow: #4fd2f0;
    --brain-deep: #0b4f78;
    --text-white: #ffffff;
    --text-soft: #e4ecf6;
  }
  * { margin: 0; padding: 0; box-sizing: border-box; }
  html, body {
    width: 1200px;
    height: 1200px;
    overflow: hidden;
    background: var(--page-bg);
  }
  .label {
    position: absolute;
    left: 80px;
    top: 20px;
    width: 1040px;
    height: 1160px;
    background: var(--label-white);
    overflow: hidden;
  }
  .label-waves {
    position: absolute;
    inset: 0;
    width: 1040px;
    height: 1160px;
  }
  .top-band {
    position: absolute;
    left: 0;
    top: 0;
    width: 100%;
    height: 75px;
    background: var(--band-orange);
  }
  .brand-tab {
    position: absolute;
    left: 232px;
    top: 0;
    width: 580px;
    height: 166px;
    background: linear-gradient(180deg, var(--tab-navy-light), var(--tab-navy));
    border-radius: 0 0 34px 34px;
    display: flex;
    align-items: center;
    justify-content: center;
    gap: 18px;
    padding-top: 10px;
  }
  .brand-dot {
    width: 38px;
    height: 38px;
    border-radius: 50%;
    background: var(--text-white);
  }
  .brand-name {
    font-family: "Open Sans", sans-serif;
    font-weight: 400;
    font-size: 62px;
    color: var(--text-white);
    letter-spacing: 0.5px;
  }
  .product-title {
    position: absolute;
    left: 0;
    width: 100%;
    text-align: center;
    font-family: "Oswald", sans-serif;
    font-weight: 700;
    color: var(--title-orange);
    background: linear-gradient(180deg, var(--title-orange), var(--title-rust));
    -webkit-background-clip: text;
    background-clip: text;
    -webkit-text-fill-color: transparent;
    line-height: 1;
  }
  .product-title--main {
    top: 218px;
    font-size: 170px;
    letter-spacing: -2px;
  }
  .product-title--sub {
    top: 400px;
    font-size: 112px;
    letter-spacing: -1px;
  }
  .brain-art {
    position: absolute;
    left: 255px;
    top: 545px;
    width: 530px;
    height: 390px;
    border-radius: 52% 48% 44% 40% / 56% 58% 42% 44%;
    background: radial-gradient(ellipse at 48% 42%, var(--brain-glow) 0%, #1d93c4 45%, var(--brain-deep) 100%);
  }
  .claim {
    position: absolute;
    left: 0;
    top: 965px;
    width: 100%;
    text-align: center;
    font-family: "Open Sans", sans-serif;
    font-weight: 700;
    font-size: 50px;
    color: var(--text-white);
  }
  .claim sup {
    font-size: 30px;
    vertical-align: 22px;
  }
  .product-info {
    position: absolute;
    left: 0;
    width: 100%;
    text-align: center;
    font-family: "Roboto Condensed", sans-serif;
    font-weight: 700;
    font-size: 33px;
    color: var(--text-soft);
    letter-spacing: 0.5px;
  }
  .product-info--type { top: 1045px; }
  .product-info--count { top: 1095px; }
</style>
</head>
<body>
  <main class="label">
    <svg class="label-waves" viewBox="0 0 1040 1160" aria-hidden="true">
      <defs>
        <linearGradient id="waveBlue" x1="0" y1="0" x2="0" y2="1">
          <stop offset="0" stop-color="var(--wave-blue)"/>
          <stop offset="1" stop-color="var(--wave-blue-deep)"/>
        </linearGradient>
      </defs>
      <path d="M0 640 C300 840 740 840 1040 640 L1040 1160 L0 1160 Z" fill="var(--wave-light)"/>
      <path d="M0 672 C300 872 740 872 1040 672 L1040 1160 L0 1160 Z" fill="var(--wave-navy)"/>
      <path d="M0 690 C300 890 740 890 1040 690 L1040 1160 L0 1160 Z" fill="url(#waveBlue)"/>
    </svg>

    <div class="top-band"></div>
    <div class="brand-tab">
      <span class="brand-dot"></span>
      <span class="brand-name">Cortiva Plus</span>
    </div>

    <h1 class="product-title product-title--main">Brain Booster</h1>
    <h2 class="product-title product-title--sub">Supplement</h2>

    <div class="brain-art" role="img" aria-label="Glowing blue illustration of a human brain with light points"></div>

    <p class="claim">Promotes Brain function<sup>*</sup></p>
    <p class="product-info product-info--type">DIETARY SUPPLEMENT</p>
    <p class="product-info product-info--count">30 CAPSULES</p>
  </main>
</body>
</html>
```